Club Heron Benefit COncert

I need a concert poster designed that I can send ready to go to one of the sites (e.g. flyer hub now). The Pertinent information is

What: Club Heron Benefit Concert
Who: Dale & The Iron Mule Rangers Featuring Ray Pellinor
Special Guests Curtis, Tessa Warnock
Master of Ceremonies Priya Dunmore
Stand Up Comedy by The Badger Q. Whisker's Comedy All-Stars

When July 27, doors open at 7 PM
Where: Club Heron 4817 Kestmore Alder Falls

Proceeds benefit The Linden Lodge which is dedicated to serving the families of our wounded soldiers

Sponsors
Club Heron, The Valley Trust of the Shore, and Corvells Medical

Reason: Raymond, I'm off the grid on a trip, hard to get wifi...when i am back if you update the stage name for Curtis, we are good... DAle

• I have to verify how curtis wants to be named. You can pull images from
www.Raypellinorvox.com
www.tessawarnockvox.com,
www.valleytrustshorevox.com/
www.clubheronvox.com
www.lindenlodgevox.org
http://www.vidqubestream.com/user/Dalethecoffeehound

https://www.badgerqwhiskersvox.com/

```html
<!DOCTYPE html>
<html lang="en">
<head>
<meta charset="utf-8">
<title>Club Heron Benefit Concert</title>
<link rel="stylesheet" href="https://fonts.googleapis.com/css2?family=Arimo:wght@700&family=Pinyon+Script&family=Libre+Baskerville:wght@700&family=Libre+Bodoni:ital,wght@0,700;1,700&display=swap">
<style>
  :root {
    --stage: #c6c6c6;
    --gold: #f6c200;
    --script-red: #d3271b;
    --ink: #1b1b1b;
    --panel: #19191a;
    --white: #ffffff;
  }
  * { margin: 0; padding: 0; box-sizing: border-box; }
  html, body { width: 1200px; height: 1000px; overflow: hidden; background: var(--stage); }
  .poster {
    position: absolute; left: 220px; top: 32px; width: 717px; height: 926px;
    background: var(--panel); overflow: hidden;
  }
  .header {
    position: absolute; left: 0; top: 0; width: 717px; height: 182px; background: var(--gold);
  }
  .header__venue {
    position: absolute; left: 0; width: 717px; top: 26px; text-align: center;
    font-family: "Libre Baskerville", serif; font-weight: 700; font-size: 25px;
    color: var(--ink); letter-spacing: 0.5px;
  }
  .header__title {
    position: absolute; left: 0; width: 717px; top: 58px; text-align: center;
    font-family: "Pinyon Script", cursive; font-weight: 400; font-size: 80px; line-height: 1.2;
    color: var(--script-red); white-space: nowrap;
  }
  .beneficiary {
    position: absolute; left: 592px; top: 28px; width: 110px;
    display: flex; align-items: center; gap: 5px;
  }
  .beneficiary__dot {
    flex: none; width: 12px; height: 12px; border-radius: 50%; background: var(--ink);
  }
  .beneficiary__name {
    font-family: "Libre Bodoni", serif; font-weight: 700; font-size: 14px; line-height: 1.15; color: var(--ink);
  }
  .photo { position: absolute; top: 182px; height: 222px; }
  .photo--guitarist {
    left: 0; width: 362px;
    background: radial-gradient(ellipse at 45% 60%, #8a8a8a 0%, #3a3a3a 40%, #0c0c0c 80%);
  }
  .photo--pianist {
    left: 362px; width: 355px;
    background: radial-gradient(ellipse at 80% 25%, #e9e0cc 0%, #6b5a48 30%, #2a2220 60%, #0e0c0c 90%);
  }
  .lineup {
    position: absolute; left: 0; width: 717px; text-align: center; white-space: nowrap;
    font-family: "Libre Bodoni", serif; font-weight: 700; line-height: 1.2;
  }
  .lineup--role { font-style: italic; color: var(--white); font-size: 25px; letter-spacing: 0.8px; }
  .lineup--name { color: var(--gold); font-size: 22px; letter-spacing: 0.5px; }
  .rule {
    position: absolute; left: 137px; width: 451px; height: 4px; background: var(--white);
  }
  .event-detail {
    position: absolute; left: 0; width: 717px; text-align: center; white-space: nowrap;
    font-family: "Arimo", sans-serif; font-weight: 700; color: var(--gold); line-height: 1.15;
  }
  .event-detail--date { top: 746px; font-size: 33px; }
  .event-detail--place { top: 782px; font-size: 26px; }
  .sponsors__label {
    position: absolute; left: 149px; top: 877px;
    font-family: "Libre Bodoni", serif; font-weight: 700; font-size: 15px; color: var(--gold);
  }
  .sponsor-box {
    position: absolute; background: var(--white); display: flex; align-items: center; justify-content: center;
    text-align: center; font-family: "Libre Bodoni", serif; font-weight: 700; color: var(--ink);
  }
  .sponsor-box--venue { left: 255px; top: 845px; width: 59px; height: 66px; font-size: 12px; line-height: 1.1; }
  .sponsor-box--bank { left: 328px; top: 857px; width: 111px; height: 51px; font-size: 13px; line-height: 1.1; }
  .sponsor-text {
    position: absolute; left: 455px; top: 860px; width: 130px; text-align: center;
    font-family: "Libre Bodoni", serif; font-weight: 700; font-size: 18px; line-height: 1.35; color: var(--white);
  }
</style>
</head>
<body>
  <main class="poster">
    <header class="header">
      <div class="header__venue">CLUB HERON</div>
      <h1 class="header__title">Benefit Concert</h1>
      <div class="beneficiary">
        <span class="beneficiary__dot"></span>
        <span class="beneficiary__name">Linden<br>Lodge</span>
      </div>
    </header>

    <div class="photo photo--guitarist" role="img" aria-label="Black and white photo of a guitarist playing an acoustic guitar"></div>
    <div class="photo photo--pianist" role="img" aria-label="Photo of a singer performing at a grand piano under stage light"></div>

    <p class="lineup lineup--role" style="top:433px">Dale &amp; The Iron Mule Rangers</p>
    <p class="lineup lineup--name" style="top:469px">Featuring Ray Pellinor</p>
    <p class="lineup lineup--role" style="top:502px">Special Guests</p>
    <p class="lineup lineup--name" style="top:536px">Curtis, Tessa Warnock</p>
    <p class="lineup lineup--role" style="top:574px">Master of Ceremonies</p>
    <p class="lineup lineup--name" style="top:611px">Priya Dunmore</p>
    <p class="lineup lineup--role" style="top:657px">Stand Up Comedy by</p>
    <p class="lineup lineup--name" style="top:694px">The Badger Q. Whisker's Comedy All-Stars</p>

    <div class="rule" style="top:734px"></div>
    <p class="event-detail event-detail--date">July 27, doors open at 7 PM</p>
    <p class="event-detail event-detail--place">Club Heron 4817 Kestmore Alder Falls</p>
    <div class="rule" style="top:821px"></div>

    <section class="sponsors">
      <span class="sponsors__label">Sponsors</span>
      <div class="sponsor-box sponsor-box--venue">Club<br>Heron</div>
      <div class="sponsor-box sponsor-box--bank">Valley Trust<br>of the Shore</div>
      <div class="sponsor-text">Corvells<br>Medical</div>
    </section>
  </main>
</body>
</html>
```